Sandwich Board and Poster design promoting a medical aesthetic clinic

I am looking for a clean, modern and relaxing design promoting a medical physician-led aesthetic clinic.
Services offered are neuromodulator treatment (Velmira) and Dermal Fillers.
Logo must be included.
Use the tag line "Refresh your look, revive your spirit."
Address is 204-205 27391 83 Ave, Surrey, V2K 4N7
604-718-2453
email - info@glowmapleco.ca
www.glowmapleco.ca

```html
<!DOCTYPE html>
<html lang="en">
<head>
<meta charset="utf-8">
<title>Lumera Aesthetics – Poster</title>
<link rel="stylesheet" href="https://fonts.googleapis.com/css2?family=Bebas+Neue&family=Lexend:wght@300;400;600&family=Montserrat:wght@500&display=swap">
<style>
  :root {
    --gold: #d8af28;
    --navy: #1f3b5e;
    --ink: #1d2a3a;
    --cream: #f4ebcc;
    --paper: #ffffff;
    --backdrop: #adadad;
  }
  * { box-sizing: border-box; margin: 0; padding: 0; }
  html, body { width: 1200px; height: 1200px; overflow: hidden; }
  body { background: var(--backdrop); position: relative; }

  .poster {
    position: absolute; left: 190px; top: 22px;
    width: 820px; height: 1156px;
    background: var(--paper); overflow: hidden;
  }

  .hero-photo {
    position: absolute; left: 350px; top: 0; width: 470px; height: 1060px;
    background:
      linear-gradient(to bottom, rgba(255,255,255,0) 70%, #fff 100%),
      linear-gradient(to right, #fff 0%, rgba(255,255,255,0) 25%),
      linear-gradient(to right, #f2dcc8 30%, #e8c9a6 55%, #a06f50 75%, #6b4632 100%);
  }

  .brand {
    position: absolute; left: 40px; top: 160px; width: 280px;
    display: flex; align-items: center; justify-content: center; gap: 12px;
  }
  .brand-dot { width: 18px; height: 18px; border-radius: 50%; background: var(--gold); }
  .brand-name {
    font-family: "Montserrat", sans-serif; font-weight: 500;
    font-size: 22px; letter-spacing: 5px; color: var(--navy);
  }

  .tagline {
    position: absolute; left: 48px; top: 288px;
    font-family: "Bebas Neue", sans-serif; line-height: 0.84;
    letter-spacing: -1px;
  }
  .tagline span { display: block; }
  .tagline .line-gold { color: var(--gold); font-size: 92px; }
  .tagline .line-navy { color: var(--navy); font-size: 92px; }
  .tagline .line-big { color: var(--gold); font-size: 188px; line-height: 0.8; letter-spacing: -3px; }

  .services {
    position: absolute; left: 48px; top: 694px;
    font-family: "Lexend", sans-serif; color: var(--navy);
    font-size: 26px; line-height: 37px;
  }
  .services .intro { font-weight: 300; }
  .services .list { font-weight: 600; }

  .treatments {
    position: absolute; left: 45px; top: 816px; width: 735px;
    display: flex; justify-content: space-between;
  }
  .treatment-photo {
    width: 226px; height: 226px; border-radius: 50%;
    border: 8px solid var(--cream);
  }
  .treatment-photo.one { background: radial-gradient(circle at 40% 45%, #f6dcc8, #e3bfa6 60%, #8fc5e8 100%); }
  .treatment-photo.two { background: radial-gradient(circle at 60% 35%, #d9a884, #8a5a3c 55%, #3a2a22 100%); }
  .treatment-photo.three { background: radial-gradient(circle at 55% 70%, #b07a58, #6a4634 50%, #3b4fa8 100%); }

  .contact {
    position: absolute; left: 54px; top: 1080px; width: 740px;
    display: flex; font-family: "Lexend", sans-serif;
    font-size: 17px; line-height: 22px; color: var(--ink);
  }
  .contact-item { display: flex; align-items: center; gap: 18px; }
  .contact-item.address { width: 284px; }
  .contact-item.phone { width: 208px; }
  .contact-icon {
    width: 28px; height: 28px; border-radius: 50%; background: var(--gold);
    display: flex; align-items: center; justify-content: center; flex: none;
  }
</style>
</head>
<body>
  <main class="poster">
    <div class="hero-photo" role="img" aria-label="Side profile portrait of two women with smooth, glowing skin"></div>

    <div class="brand">
      <span class="brand-dot"></span>
      <span class="brand-name">LUMERA AESTHETICS</span>
    </div>

    <h1 class="tagline">
      <span class="line-gold">Refresh</span>
      <span class="line-navy">Your Look</span>
      <span class="line-navy">Revive Your</span>
      <span class="line-big">Spirit</span>
    </h1>

    <p class="services">
      <span class="intro">Services offered are</span><br>
      <span class="list">Neuromodulator treatment (Velmira)<br>and Dermal Fillers.</span>
    </p>

    <div class="treatments">
      <div class="treatment-photo one" role="img" aria-label="Client receiving a brow-area injection"></div>
      <div class="treatment-photo two" role="img" aria-label="Practitioner applying forehead injection treatment"></div>
      <div class="treatment-photo three" role="img" aria-label="Gloved hands performing a dermal filler treatment"></div>
    </div>

    <footer class="contact">
      <div class="contact-item address">
        <span class="contact-icon">
          <svg width="14" height="16" viewBox="0 0 14 16"><path d="M7 1a5 5 0 0 0-5 5c0 3.6 5 9 5 9s5-5.4 5-9a5 5 0 0 0-5-5z" fill="#1f3b5e"/><circle cx="7" cy="6" r="1.8" fill="#d8af28"/></svg>
        </span>
        <span>204-205 27391 83 AVE,<br>SURREY, V2K 4N7</span>
      </div>
      <div class="contact-item phone">
        <span class="contact-icon">
          <svg width="14" height="14" viewBox="0 0 14 14"><path d="M3 1l2 3-1.3 1.3a8 8 0 0 0 5 5L10 9l3 2-1 2.4C6 13.5.6 8 .6 2z" fill="#1f3b5e"/></svg>
        </span>
        <span>CALL US:<br>604-718-2453</span>
      </div>
      <div class="contact-item web">
        <span class="contact-icon">
          <svg width="16" height="16" viewBox="0 0 16 16" fill="none" stroke="#1f3b5e" stroke-width="1.4"><circle cx="8" cy="8" r="6.3"/><ellipse cx="8" cy="8" rx="2.8" ry="6.3"/><path d="M1.7 8h12.6M2.6 5h10.8M2.6 11h10.8"/></svg>
        </span>
        <span>info@glowmapleco.ca<br>www.glowmapleco.ca</span>
      </div>
    </footer>
  </main>
</body>
</html>
```